Tovlen Systems New Website - IT Infrastructure | Smart Cabinet | Micro Data Center

We're an IT SI providing Server Room Design & Build | All-in-One Rack & Smart Cabinet | Structured Cabling | IT Relocation | Maintenance. Old website can be found at www.tovlensys.com.hk. We'd like a brand new wix website which is modern, minimalist, interactive with some animation. Website content will be mostly static and include our service, our project, news and events, about us, contacts, blogs, partners and brands, etc.

reference sites:
We'd like to see more designs referring to below

https://www.pixelbazar.example/design/51730264
https://www.pixelbazar.example/design/51869047
https://vellhorn.example/

Animation (scrolling effect) referring to
https://vellhorn.example/intelligence/smart-office-room/
Updates

we'd like below style.

Designs look the same

Target Market(s)

Commercials in HK

Industry/Entity Type

IT, Technology, Data Center

Coding

Coded - Design and coding required

Font styles to use
Sans Serif

Requirements
Must have
• CMS, Some Interactive Elements/ Graphics

```html
<!DOCTYPE html>
<html lang="en">
<head>
<meta charset="utf-8">
<title>Tovlen Systems</title>
<link href="https://fonts.googleapis.com/css2?family=Oxanium:wght@500;600;700&family=Poppins:wght@400;500;600&display=swap" rel="stylesheet">
<style>
:root{
  --red:#c4161c;
  --red-dark:#9e1015;
  --navy:#0e1733;
  --hero:#141923;
  --blue:#163463;
  --ink:#1c1c2a;
  --text:#4a4a55;
  --muted:#eef0f6;
  --card:#f0f1f3;
  --white:#ffffff;
}
*{box-sizing:border-box;margin:0;padding:0}
html,body{width:1200px;height:4886px;overflow:hidden}
body{position:relative;background:var(--white);font-family:"Poppins",sans-serif;color:var(--text)}
.abs{position:absolute}
.head{font-family:"Oxanium",sans-serif;font-weight:600;color:var(--ink)}
.btn{position:absolute;display:flex;align-items:center;justify-content:center;gap:6px;background:var(--red);color:#fff;font:600 12px "Poppins",sans-serif;text-transform:uppercase;letter-spacing:.3px}
.btn.outline{box-shadow:4px 4px 0 -1px #fff,5px 5px 0 0 var(--red)}
.arrow-dot{width:11px;height:11px;border-radius:50%;background:#fff;display:inline-flex;align-items:center;justify-content:center}
.arrow-dot::after{content:"";border-left:4px solid var(--red);border-top:3px solid transparent;border-bottom:3px solid transparent;margin-left:1px}
.photo{position:absolute}
.brand{position:absolute;display:flex;align-items:center;gap:10px;font:600 30px "Oxanium",sans-serif;color:var(--ink)}
.brand .mark{width:30px;height:30px;border:3px solid var(--ink)}
.nav{position:absolute;top:24px;left:432px;display:flex;gap:38px;font-size:13px;color:#555}
.nav .on{color:var(--red)}
.hero-kicker{left:104px;top:234px;font:600 18px "Oxanium",sans-serif;color:var(--red)}
.hero-title{left:104px;top:262px;font:700 50px/58px "Oxanium",sans-serif;color:#fff}
.hero-title span{color:var(--red)}
.hero-copy{left:104px;top:396px;width:330px;font-size:10px;line-height:17.5px;color:#e6e6ea}
.dots{position:absolute;left:1140px;top:350px;display:flex;flex-direction:column;gap:9px}
.dots i{width:11px;height:11px;border-radius:50%;background:#fff;display:block}
.dots i.on{background:var(--red)}
.about-title{left:621px;top:815px;font:600 34px/42px "Oxanium",sans-serif}
.about-copy{left:621px;top:910px;width:482px;font-size:12px;line-height:22.5px}
.sec-title{position:absolute;left:0;width:1200px;text-align:center;font:600 33px "Oxanium",sans-serif}
.svc{position:absolute;top:1458px;width:250px;height:262px}
.svc .lbl{position:absolute;left:16px;bottom:22px;font:700 16px/26px "Oxanium",sans-serif;color:#fff}
.svc.active{background:var(--red);height:322px;padding:46px 16px}
.svc.active h3{font:700 17px/26px "Oxanium",sans-serif;color:#fff}
.svc.active p{margin-top:16px;font-size:10.5px;line-height:21.5px;color:#f6dede}
.proj-lbl{position:absolute;left:14px;bottom:22px;font:700 16px/24px "Oxanium",sans-serif;color:#fff}
.partner{position:absolute;top:2758px;width:186px;height:68px;background:#fff;display:flex;align-items:center;justify-content:center}
.partner i{display:block;width:110px;height:18px;background:#c8cad0;border-radius:3px}
.news{position:absolute;top:3102px;width:476px;height:158px;background:#fff;border-radius:4px}
.news h4{position:absolute;left:166px;top:20px;font:600 18px "Oxanium",sans-serif;color:var(--ink)}
.news .meta{position:absolute;left:166px;top:54px;font:600 11px "Poppins",sans-serif;color:var(--ink);display:flex;gap:16px}
.news p{position:absolute;left:166px;top:80px;width:290px;font-size:11px;line-height:22px}
.blog{position:absolute;top:3558px;width:317px;height:378px;background:var(--card)}
.blog h4{position:absolute;left:22px;top:228px;font:600 20px "Oxanium",sans-serif;color:var(--ink)}
.blog p{position:absolute;left:22px;top:265px;width:275px;font-size:11px;line-height:22.5px}
.blog a{position:absolute;left:22px;top:338px;font-size:12px;font-weight:600;color:var(--red);text-decoration:underline}
.field{position:absolute;background:#eef0f8;border-radius:12px;font-size:13px;color:#555;padding:14px 20px}
.foot-h{position:absolute;top:4587px;font:600 19px "Oxanium",sans-serif;color:var(--ink)}
.foot-list{position:absolute;top:4624px;list-style:none;font-size:12px;line-height:30px;color:#666}
.foot-list .on{color:var(--red)}
.ci{position:absolute;left:802px;width:22px;height:22px;border-radius:50%;background:var(--red)}
.ct{position:absolute;left:846px;font-size:12px;line-height:20px;color:#666;width:260px}
</style>
</head>
<body>

<!-- HERO BACKGROUND -->
<div class="photo" style="left:0;top:0;width:1200px;height:712px;background:radial-gradient(ellipse at 50% 40%,#2a3040 0%,var(--hero) 55%,#0b0e15 100%)" role="img" aria-label="Dim data-centre server aisle behind the hero"></div>
<svg class="abs" style="left:0;top:0" width="1200" height="740" viewBox="0 0 1200 740">
  <polygon points="0,0 1200,0 1200,64 300,64 264,100 0,100" fill="#fff"/>
  <polygon points="0,705 640,705 665,690 1200,690 1200,712 670,712 645,740 0,740" fill="#fff"/>
  <polyline points="0,702 638,702 662,686 1200,686" fill="none" stroke="var(--red)" stroke-width="5"/>
  <polyline points="0,714 644,714 668,700 1200,700" fill="none" stroke="#7a1014" stroke-width="2"/>
</svg>

<!-- HEADER -->
<div class="brand" style="left:66px;top:30px"><span class="mark"></span>Tovlen</div>
<nav class="nav"><span class="on">Home</span><span>About</span><span>Our Services</span><span>Our Projects</span><span>Contact Us</span></nav>
<div class="btn outline" style="left:978px;top:12px;width:114px;height:38px">Log In <span class="arrow-dot"></span></div>

<!-- HERO CONTENT -->
<div class="abs hero-kicker">Welcome To</div>
<div class="abs hero-title"><span>Tovlen</span><br>Systems</div>
<p class="abs hero-copy">Tovlen Systems is well experienced in delivering the best in Data Center Infrastructure, Network Infrastructure, Structured Cabling, Telephony, Access Control, Video Surveillance, Audiovisual &amp; Conferencing, Relocation Migration and Maintenance solutions.</p>
<div class="btn outline" style="left:104px;top:486px;width:172px;height:44px">Get Started <span class="arrow-dot"></span></div>
<div class="photo" style="left:646px;top:186px;width:394px;height:396px;border-radius:14px;border:2px solid #cfd6e4;background:linear-gradient(135deg,#34496b,#1c2840)" role="img" aria-label="Two engineers checking a tablet in a server room"></div>
<div class="dots"><i class="on"></i><i></i><i></i><i></i></div>
<svg class="abs" style="left:578px;top:696px" width="44" height="44" viewBox="0 0 44 44">
  <circle cx="22" cy="22" r="20" fill="#fff" stroke="#ddd"/>
  <path d="M22 14v14M16 23l6 6 6-6" stroke="var(--red)" stroke-width="2.5" fill="none"/>
</svg>

<!-- ABOUT -->
<div class="photo" style="left:100px;top:835px;width:372px;height:372px;background:linear-gradient(135deg,#3a3f55,#7d8597 60%,#c9ccd4);border-radius:4px" role="img" aria-label="Technician patching network cables"></div>
<div class="abs" style="left:547px;top:822px;width:1px;height:330px;background:#d6d6de"></div>
<h2 class="abs head about-title">About<br>Tovlen Systems</h2>
<p class="abs about-copy">Tovlen Systems is well experienced in delivering the best in Data Center Infrastructure, Network Infrastructure, Structured Cabling, Telephony, Access Control, Video Surveillance, Audiovisual &amp; Conferencing, Relocation &amp; Migration and Maintenance solutions. Our dedication, focus, and expertise wins much recognition of many IT professionals in all industries in the region. In Tovlen Systems's Belief, the major reason that we gain a lot of true long-lasting business relationship with our clients was that we offer them the attention, consideration, passion, and professionalism that they deserved.</p>
<div class="btn outline" style="left:621px;top:1130px;width:150px;height:44px">Read More <span class="arrow-dot"></span></div>

<!-- SERVICES -->
<svg class="abs" style="left:0;top:1285px" width="1200" height="605" viewBox="0 0 1200 605">
  <defs><linearGradient id="svcbg" x1="0" y1="0" x2="0" y2="1"><stop offset="0" stop-color="#1e3f74"/><stop offset="1" stop-color="#0f2750"/></linearGradient></defs>
  <polygon points="0,100 95,0 1200,0 1200,510 1108,605 0,605" fill="url(#svcbg)"/>
</svg>
<h2 class="sec-title" style="top:1350px;color:#fff">Our Services</h2>
<div class="svc photo" style="left:72px;background:linear-gradient(180deg,#5c6470,#1d232c)" role="img" aria-label="Data centre hall with rack rows"><div class="lbl">Data Center<br>Design And Build</div></div>
<div class="svc photo" style="left:340px;background:linear-gradient(180deg,#4a6f9a,#1b2a3f)" role="img" aria-label="Blue structured cabling in racks"><div class="lbl">Structured Cabling<br>And Fiber Backbone</div></div>
<div class="svc active" style="left:608px">
  <h3>All-In-One Rack /<br>Micro – Data Center</h3>
  <p>Tovlen offers adaptive IT hardware support maintenance service to our customer in order to extend hardware lifecycles and maintain uptime. Our service provides highly skilled technical personnel.</p>
  <div class="btn outline" style="left:16px;top:260px;width:150px;height:42px;background:#fff;color:var(--red);box-shadow:none">Read More <span class="arrow-dot" style="background:var(--red)"></span></div>
</div>
<div class="svc photo" style="left:876px;background:linear-gradient(180deg,#9aa1aa,#3a4048)" role="img" aria-label="Empty conference room with screens"><div class="lbl">Audiovisual and<br>Conference</div></div>

<!-- PROJECTS -->
<h2 class="abs head" style="left:104px;top:1958px;font-size:33px">Our Projects</h2>
<p class="abs" style="left:104px;top:2014px;width:450px;font-size:11.5px;line-height:21px">Lorem ipsum dolor sit amet, consectetur adipiscing elit, sed do eiusmod tempor incididunt ut labore et dolore magna aliqua. Quis ipsum suspendisse ultrices gravida.</p>
<div class="btn outline" style="left:104px;top:2095px;width:156px;height:42px">Learn More <span class="arrow-dot"></span></div>
<div class="photo" style="left:600px;top:1965px;width:242px;height:278px;background:linear-gradient(180deg,#4d5968,#1c222b)" role="img" aria-label="Open network cabinet"><div class="proj-lbl">A Renowned China<br>Based Listed Insurance<br>Company</div></div>
<div class="photo" style="left:852px;top:1965px;width:243px;height:278px;background:linear-gradient(180deg,#3e6ea8,#162843)" role="img" aria-label="Dense blue patch cables"><div class="proj-lbl">Orient Sourcing</div></div>
<div class="photo" style="left:104px;top:2253px;width:491px;height:257px;background:linear-gradient(100deg,#233b66,#3d5a88 45%,#1a1f28)" role="img" aria-label="Cable bundles along a rack"><div class="proj-lbl">Harbour Crest International &amp; Meridian</div></div>
<div class="photo" style="left:605px;top:2253px;width:490px;height:257px;background:linear-gradient(100deg,#2a2e35,#50565f 50%,#1b1e23)" role="img" aria-label="Smart cabinets with touch displays"><div class="proj-lbl">A Renown China Based Securities Firm</div></div>

<!-- PARTNERS -->
<div class="abs" style="left:0;top:2590px;width:1200px;height:322px;background:var(--muted)"></div>
<h2 class="sec-title" style="top:2666px;color:var(--ink)">Our Partners</h2>
<div class="partner" style="left:-98px"><i></i></div>
<div class="partner" style="left:100px"><i></i></div>
<div class="partner" style="left:300px"><i></i></div>
<div class="partner" style="left:502px;box-shadow:0 4px 14px rgba(0,0,0,.12)"><i></i></div>
<div class="partner" style="left:702px"><i></i></div>
<div class="partner" style="left:904px"><i></i></div>
<div class="partner" style="left:1106px"><i></i></div>

<!-- NEWS -->
<svg class="abs" style="left:0;top:2935px" width="1200" height="470" viewBox="0 0 1200 470">
  <defs><linearGradient id="newsbg" x1="0" y1="0" x2="0" y2="1"><stop offset="0" stop-color="#b8161b"/><stop offset="1" stop-color="#8f0e12"/></linearGradient></defs>
  <polygon points="0,85 95,0 1200,0 1200,380 1105,470 0,470" fill="url(#newsbg)"/>
</svg>
<h2 class="sec-title" style="top:3005px;color:#fff">News And Events</h2>
<div class="news" style="left:115px">
  <div class="photo" style="left:4px;top:4px;width:146px;height:150px;background:linear-gradient(135deg,#6a7787,#2b323d)" role="img" aria-label="Engineer working at a server rack"></div>
  <h4>Lorem Ipsum</h4>
  <div class="meta"><span>▦ 19Dec – 2023</span><span>● Kai Wong</span></div>
  <p>Lorem ipsum dolor sit amet, consectetur elit, sed do eiusmod tempor incididunt aliqua.</p>
</div>
<div class="news" style="left:610px">
  <div class="photo" style="left:4px;top:4px;width:146px;height:150px;background:linear-gradient(135deg,#3a4150,#14171d)" role="img" aria-label="Row of dark server cabinets"></div>
  <h4>Lorem Ipsum</h4>
  <div class="meta"><span>▦ 19Dec – 2023</span><span>● Kai Wong</span></div>
  <p>Lorem ipsum dolor sit amet, consectetur elit, sed do eiusmod tempor incididunt aliqua.</p>
</div>
<div class="abs" style="left:578px;top:3306px;display:flex;gap:12px"><i style="width:11px;height:11px;border-radius:50%;background:#fff;display:block"></i><i style="width:11px;height:11px;border-radius:50%;border:2px solid #fff;display:block"></i></div>

<!-- BLOGS -->
<h2 class="sec-title" style="top:3470px;color:var(--ink)">Our Blogs</h2>
<div class="blog" style="left:104px">
  <div class="photo" style="left:0;top:0;width:317px;height:205px;background:linear-gradient(135deg,#1b1b24,#4a3f6b)" role="img" aria-label="Blog cover: enclosed rack aisle graphic"></div>
  <h4>Lorem Ipsum</h4><p>Lorem ipsum dolor sit amet, consectetur adipiscing elit, sed do eiusmod tempor incididunt ut labore et dolore magna aliqua.</p><a>Read More</a>
</div>
<div class="blog" style="left:441px">
  <div class="photo" style="left:0;top:0;width:317px;height:205px;background:linear-gradient(180deg,#b9c4cc,#7d8a6a 60%,#d49a3c)" role="img" aria-label="Blog cover: cabinet in an open landscape"></div>
  <h4>Lorem Ipsum</h4><p>Lorem ipsum dolor sit amet, consectetur adipiscing elit, sed do eiusmod tempor incididunt ut labore et dolore magna aliqua.</p><a>Read More</a>
</div>
<div class="blog" style="left:778px">
  <div class="photo" style="left:0;top:0;width:317px;height:205px;background:linear-gradient(90deg,#2a2350,#5b6e3a)" role="img" aria-label="Blog cover: cabinet among green trees"></div>
  <h4>Lorem Ipsum</h4><p>Lorem ipsum dolor sit amet, consectetur adipiscing elit, sed do eiusmod tempor incididunt ut labore et dolore magna aliqua.</p><a>Read More</a>
</div>

<!-- CONTACT -->
<svg class="abs" style="left:0;top:4012px" width="1200" height="510" viewBox="0 0 1200 510">
  <defs><linearGradient id="ctbg" x1="0" y1="0" x2="0" y2="1"><stop offset="0" stop-color="#1a2340"/><stop offset="1" stop-color="#0e1733"/></linearGradient></defs>
  <polygon points="0,60 62,0 1200,0 1200,510 0,510" fill="url(#ctbg)"/>
  <polygon points="1200,430 1120,510 1200,510" fill="#fff"/>
</svg>
<h2 class="sec-title" style="top:4084px;color:#fff">Contacts Us</h2>
<div class="field" style="left:135px;top:4180px;width:420px;height:48px">Name</div>
<div class="field" style="left:135px;top:4244px;width:420px;height:48px">Email</div>
<div class="field" style="left:135px;top:4308px;width:420px;height:48px">Phone Number</div>
<div class="field" style="left:568px;top:4180px;width:420px;height:176px">Messge</div>
<div class="btn" style="left:535px;top:4410px;width:130px;height:40px">Submit <span class="arrow-dot"></span></div>

<!-- FOOTER -->
<div class="brand" style="left:104px;top:4598px"><span class="mark"></span>Tovlen</div>
<span class="abs" style="left:104px;top:4680px;width:24px;height:24px;border-radius:50%;background:var(--red)"></span>
<span class="abs" style="left:146px;top:4680px;width:24px;height:24px;border-radius:50%;background:var(--red)"></span>
<h3 class="foot-h" style="left:350px">Quick Links</h3>
<ul class="foot-list" style="left:352px"><li class="on">Home</li><li>About</li><li>Our Services</li><li>Our Projects</li><li>Contact Us</li></ul>
<h3 class="foot-h" style="left:513px">Sercvices</h3>
<ul class="foot-list" style="left:515px"><li>Server Room Design &amp; Build</li><li>All &amp; in &amp; One Rack &amp; Smart Cabinet</li><li>Structured Cabling</li><li>IT Relocation</li><li>Maintenance</li></ul>
<h3 class="foot-h" style="left:800px">Contact Us</h3>
<span class="ci" style="top:4630px"></span><p class="ct" style="top:4626px">Rm 1508, 15/F, Harbourline Plaza, 8 Lok Wan Street, San Po Kong, Kowloon, Hong Kong</p>
<span class="ci" style="top:4696px"></span><p class="ct" style="top:4697px">marketing@tovlensys.com.hk</p>
<span class="ci" style="top:4734px"></span><p class="ct" style="top:4735px">+852 2000 1400 / +852 5000 3711</p>
<span class="ci" style="top:4772px"></span><p class="ct" style="top:4773px">+852 3000 0822</p>
<div class="abs" style="left:104px;top:4852px;width:991px;height:1px;background:#cfcfd6"></div>
<p class="abs" style="left:0;top:4862px;width:1200px;text-align:center;font-size:11px;color:#666">© Copyrights 2023 Tovlen Systems | All Rights Reserved</p>

</body>
</html>
```